Business Card Design

We sell fish products to corporate food companies who then turn these products into final food products for consumers

Industry/Entity Type

Business

Contact Information for Business Card

I need a corporate business card template for a fish products business. We would like it be professional for use in dealing with multi national companies. This company business card template will be used by multiple employees so the following fields must be open to edit (Name, Phone Number and Email address)

```html
<!DOCTYPE html>
<html lang="en">
<head>
<meta charset="utf-8">
<title>Tidewater Harvest — Business Card</title>
<link href="https://fonts.googleapis.com/css2?family=Tinos:wght@400;700&display=swap" rel="stylesheet">
<style>
  :root {
    --backdrop: #e9e6e1;
    --card: #ffffff;
    --card-shade: #e6e7ea;
    --brand-blue: #0d55a3;
    --ink-blue: #1a4f9c;
    --band-text: #e8eef8;
    --divider: #2a4a8c;
  }
  * { margin: 0; padding: 0; box-sizing: border-box; }
  html, body {
    width: 1200px; height: 892px; overflow: hidden;
    background: var(--backdrop);
    font-family: "Tinos", "Times New Roman", serif;
  }
  .business-card {
    position: absolute; left: 100px; top: 160px;
    width: 1000px; height: 571px;
    background: linear-gradient(180deg, var(--card) 0%, var(--card-shade) 100%);
    box-shadow: 0 12px 30px rgba(0,0,0,0.25);
    overflow: hidden;
  }
  .brand {
    position: absolute; left: 20px; top: 0; width: 440px; height: 490px;
    display: flex; align-items: center; justify-content: center; gap: 16px;
  }
  .brand-dot {
    width: 40px; height: 40px; border-radius: 50%;
    background: var(--brand-blue); flex: none;
  }
  .brand-name {
    font-size: 44px; font-weight: 400; color: var(--brand-blue);
    letter-spacing: 0.5px; line-height: 1; white-space: nowrap;
  }
  .divider {
    position: absolute; left: 490px; top: 70px;
    width: 2px; height: 400px;
    background: linear-gradient(180deg, rgba(42,74,140,0) 0%, var(--divider) 45%, rgba(42,74,140,0) 100%);
  }
  .contact {
    position: absolute; left: 560px; top: 110px; width: 420px; color: var(--ink-blue);
  }
  .employee-name { font-size: 50px; font-weight: 400; line-height: 1; white-space: nowrap; }
  .employee-role { font-size: 17px; margin-top: 6px; margin-left: 148px; }
  .contact-line { font-size: 23px; line-height: 1.55; white-space: nowrap; }
  .contact-lines { margin-top: 78px; margin-left: 150px; }
  .address-band {
    position: absolute; left: 0; bottom: 0; width: 100%; height: 82px;
    background: var(--brand-blue);
    display: flex; align-items: center; justify-content: center;
    color: var(--band-text); font-size: 24px; letter-spacing: 0.3px;
  }
</style>
</head>
<body>
  <div class="business-card">
    <div class="brand">
      <span class="brand-dot"></span>
      <span class="brand-name">Tidewater Harvest</span>
    </div>
    <div class="divider"></div>
    <div class="contact">
      <h1 class="employee-name">Employee name</h1>
      <p class="employee-role">Managing Director</p>
      <div class="contact-lines">
        <p class="contact-line">555-0142 0000</p>
        <p class="contact-line">info@tidewater.example</p>
      </div>
    </div>
    <div class="address-band">Office 4, 18 Harbour Row, Portside, ST 00000</div>
  </div>
</body>
</html>
```